New business card for QT4 Linkway, a marketing company.

We need a new business card design. We would like it to be blue gray and white. We would like some movement but in a more subtle pattern than in the file we uploaded. We are a marketing company that connects brands with their target audiences - we make connections. We work in the New York Metro area with sophisticated clients. The card should feel modern, upscale and professional.

Target Market(s)

Businesses looking to grow their brands in tourism and nightlife. We work with liquor and beer companies and with Tourism bureaus and companies.

Industry/Entity Type

Marketing

Contact Information for Business Card

Would like a horizontal layout, two-sided. Would like the logo on the back with the tagline ' "connecting brands to their target audiences" under the logo. On the front, we would like name, title, contact email, contact phone, website.

Font styles to use
Sans Serif

Colors
3377b5
85cae6
ffffff

Requirements
Must have
• Our logo. See attached. Otherwise, open to your ideas.
Should not have
• No colors we don't want - no reds/pinks/oranges please

```html
<!DOCTYPE html>
<html lang="en">
<head>
<meta charset="utf-8">
<title>QT4 Linkway – Business Card</title>
<link href="https://fonts.googleapis.com/css2?family=Questrial&display=swap" rel="stylesheet">
<style>
  :root {
    --backdrop: #9b9b9b;
    --paper: #ffffff;
    --brand-blue: #0b5582;
    --brand-gray: #a3a3a3;
    --icon-gray: #9a9a9a;
  }
  * { box-sizing: border-box; }
  html, body {
    margin: 0;
    width: 900px;
    height: 1200px;
    overflow: hidden;
    background: var(--backdrop);
    font-family: "Questrial", "Century Gothic", sans-serif;
  }
  .card {
    position: absolute;
    left: 0;
    width: 900px;
  }
  .card-front {
    top: 45px;
    height: 513px;
    background: var(--paper);
  }
  .card-back {
    top: 623px;
    height: 514px;
    background: var(--brand-blue);
  }

  /* Company name set as plain text */
  .company-name {
    position: absolute;
    margin: 0;
    color: var(--brand-gray);
    white-space: nowrap;
    font-weight: 400;
    letter-spacing: 0.02em;
    line-height: 1;
  }
  .company-name-front {
    left: 36px;
    top: 70px;
    font-size: 28px;
  }
  .company-name-back {
    left: 0;
    right: 0;
    top: 228px;
    text-align: center;
    font-size: 60px;
  }

  /* Front bands */
  .name-band {
    position: absolute;
    left: 0;
    top: 200px;
    width: 363px;
    height: 113px;
    background: var(--brand-blue);
    color: var(--paper);
    text-align: center;
    padding-top: 34px;
  }
  .person-name {
    margin: 0;
    font-size: 30px;
    font-weight: 400;
    letter-spacing: 0.02em;
    line-height: 1;
  }
  .person-title {
    margin: 8px 0 0;
    font-size: 16px;
    letter-spacing: 0.03em;
  }
  .accent-block {
    position: absolute;
    left: 819px;
    top: 200px;
    width: 81px;
    height: 113px;
    background: var(--brand-blue);
  }

  /* Contact list */
  .contact-list {
    position: absolute;
    left: 381px;
    top: 204px;
    margin: 0;
    padding: 0;
    list-style: none;
    color: var(--brand-blue);
  }
  .contact-item {
    display: flex;
    align-items: center;
    height: 28px;
    margin-bottom: 11px;
  }
  .contact-icon {
    width: 23px;
    height: 23px;
    margin-right: 8px;
    flex: none;
  }
  .contact-phone { font-size: 21px; }
  .contact-email, .contact-web { font-size: 25px; }

  /* Back */
  .tagline {
    position: absolute;
    left: 0;
    right: 0;
    top: 457px;
    margin: 0;
    text-align: center;
    color: var(--brand-gray);
    font-size: 23px;
    letter-spacing: 0.01em;
  }
</style>
</head>
<body>

  <section class="card card-front" aria-label="Front of business card">
    <p class="company-name company-name-front">QT4 LINKWAY</p>

    <div class="name-band">
      <h1 class="person-name">EVAN CALDER</h1>
      <p class="person-title">DIRECTOR</p>
    </div>

    <ul class="contact-list">
      <li class="contact-item contact-phone">
        <svg class="contact-icon" viewBox="0 0 24 24" aria-hidden="true">
          <rect width="24" height="24" rx="4" fill="var(--icon-gray)"/>
          <path d="M5 9c0-2 3-3 7-3s7 1 7 3v1h-3V8.5c-1-.5-2.5-.7-4-.7s-3 .2-4 .7V10H5z" fill="var(--brand-blue)"/>
          <path d="M7 11h10l1.5 7h-13z" fill="var(--brand-blue)"/>
          <circle cx="12" cy="14.5" r="1.8" fill="var(--icon-gray)"/>
        </svg>
        <span>555 014 2297</span>
      </li>
      <li class="contact-item contact-email">
        <svg class="contact-icon" viewBox="0 0 24 24" aria-hidden="true">
          <rect width="24" height="24" rx="4" fill="var(--icon-gray)"/>
          <rect x="4" y="7" width="16" height="11" fill="var(--brand-blue)"/>
          <path d="M4 7l8 6 8-6" fill="none" stroke="var(--icon-gray)" stroke-width="1.3"/>
        </svg>
        <span>hello@qt4linkway.com</span>
      </li>
      <li class="contact-item contact-web">
        <svg class="contact-icon" viewBox="0 0 24 24" aria-hidden="true">
          <rect width="24" height="24" rx="4" fill="var(--icon-gray)"/>
          <g fill="none" stroke="var(--brand-blue)" stroke-width="1.2">
            <circle cx="12" cy="12" r="7"/>
            <ellipse cx="12" cy="12" rx="3" ry="7"/>
            <path d="M5 12h14M6 8.5h12M6 15.5h12"/>
          </g>
        </svg>
        <span>www.qt4linkway.com</span>
      </li>
    </ul>

    <div class="accent-block"></div>
  </section>

  <section class="card card-back" aria-label="Back of business card">
    <p class="company-name company-name-back">QT4 LINKWAY</p>
    <p class="tagline">••• connecting brands to their target audiences</p>
  </section>

</body>
</html>
```